billboard campaign Meridale Flyers Guild

We want to run a targeted billboard campaign during the Harvest Cup in Las Vegas. The Meridale Flyers Guild is in prolonged contract negotiations with management. We want to bring public attention to our negotiations and pressure on the company to negotiate more quickly. Meridale Air owns the naming rights to "Meridale Stadium" in vegas where the harvest cup will be held. We would like artwork for this campaign that will be displayed on multiple billboards around the stadium and las vegas strip, and are seeking help in its design.
We would like to use a word play on the phrase "Big Game" which is frequently used as a alternative in advertising in reference to the Harvest Cup. Our initial thought was a simple billboard incorporating our colors and with our logo saying " Our Contract, Is Not a Big Game!" or "Meridale Flyer's Futures Are Not A Big Game!" But we are open to other suggestions and slogans. In the past we have used some artwork for picketing event which I will include for reference for logo and color scheme. The Local 4637 Haulworkers logo and union name must appear in the artwork. "Meridale Flyers Guild Haulworkers Local 4637"

Target Market(s)

Harvest Cup Attendees, Las Vegas tourists

Industry/Entity Type

aviation, labor union

Colors

Designer to choose colors to be used in the design.

Requirements
Must have
• The colors of the union logo must be those used in the included pdf art examples.

```html
<!DOCTYPE html>
<html lang="en">
<head>
<meta charset="utf-8">
<title>Meridale Flyers Guild — Billboard</title>
<link href="https://fonts.googleapis.com/css2?family=Anton&family=Roboto+Condensed:wght@700&display=swap" rel="stylesheet">
<style>
  :root {
    --stage-grey: #a09e9e;
    --union-navy: #233870;
    --union-gold: #f2b420;
    --paper-white: #ffffff;
  }
  html, body {
    margin: 0;
    padding: 0;
    width: 1200px;
    height: 436px;
    overflow: hidden;
    background: var(--stage-grey);
  }
  .billboard {
    display: block;
    width: 1200px;
    height: 436px;
  }
  .board-frame { fill: var(--union-navy); stroke: #c9c9d4; stroke-width: 1; }
  .card-back { fill: var(--union-gold); }
  .card-front { fill: var(--paper-white); }
  .slogan {
    font-family: "Anton", "Oswald", sans-serif;
    text-transform: uppercase;
  }
  .slogan-shadow { fill: var(--union-gold); }
  .slogan-face { fill: var(--union-navy); }
  .union-seal { fill: none; stroke: var(--union-gold); stroke-width: 6; }
  .union-seal-name,
  .union-credit {
    font-family: "Roboto Condensed", "Arial Narrow", sans-serif;
    font-weight: 700;
    fill: var(--paper-white);
    text-anchor: middle;
    text-transform: uppercase;
  }
  .union-seal-name { font-size: 19px; }
  .union-credit { font-size: 27px; }
</style>
</head>
<body>
<svg class="billboard" viewBox="0 0 1500 545" xmlns="http://www.w3.org/2000/svg" role="img" aria-label="Billboard: Our contract, is not a big game! Meridale Flyers Guild, Haulworkers Local 4637">
  <defs>
    <clipPath id="board-clip">
      <rect x="96" y="82" width="1308" height="381"/>
    </clipPath>
  </defs>

  <rect class="board-frame" x="96" y="82" width="1308" height="381"/>

  <g clip-path="url(#board-clip)">
    <polygon class="card-back" points="137,143 1068,78 1092,408 160,478"/>
    <polygon class="card-front" points="130,182 1058,112 1086,394 152,470"/>

    <g class="slogan" transform="rotate(-4.3 600 300)">
      <text class="slogan-shadow" x="168" y="276" font-size="96" textLength="826" lengthAdjust="spacingAndGlyphs">Our Contract, Is Not a</text>
      <text class="slogan-face" x="174" y="271" font-size="96" textLength="826" lengthAdjust="spacingAndGlyphs">Our Contract, Is Not a</text>
      <text class="slogan-shadow" x="164" y="438" font-size="178" textLength="858" lengthAdjust="spacingAndGlyphs">Big Game!</text>
      <text class="slogan-face" x="172" y="431" font-size="178" textLength="858" lengthAdjust="spacingAndGlyphs">Big Game!</text>
    </g>
  </g>

  <g class="union-mark">
    <circle class="union-seal" cx="1240" cy="220" r="70"/>
    <text class="union-seal-name" x="1240" y="227">Haulworkers</text>
  </g>

  <g class="union-credits">
    <text class="union-credit" x="1240" y="352">Meridale Flyers</text>
    <text class="union-credit" x="1240" y="385">Guild</text>
    <text class="union-credit" x="1240" y="418">Haulworkers Local 4637</text>
  </g>
</svg>
</body>
</html>
```